Corvimo Business Card

Corvimo is a young and energetic software development consultancy. We spend our time on the road working with clients on their sites an meeting new potential customers and employees!

We need a sharp, vibrant and memorable business card that will inspires those that receive it to look after it as it oozes quality and is a nice thing in its own right.

We like bold colours and distinctive design. So show us what you can do.

In terms of information on the card, it would be good to see:

* Our logo (Obviously :) )
* Employee name
* Email
* Website address
* Mobile number
* Full company name (Corvimo ltd)
* Registered company number
* Registered company address

Industry/Entity Type

Software

Requirements
Nice to have
• We are thinking that having a QR Code on the business card could be a good way of adding active marketing. It would be good to see if you are able to merge the kind of element in to your designs!

Maybe something special could be achieved using a visual QR Code like those produced at http://www.pixoranta.example/ ? You have our media so feel free to have a play.

```html
<!DOCTYPE html>
<html lang="en">
<head>
<meta charset="utf-8">
<title>Corvimo Business Card</title>
<link href="https://fonts.googleapis.com/css2?family=Open+Sans:wght@400;600;700&display=swap" rel="stylesheet">
<style>
  :root {
    --page: #ecebe8;
    --card-white: #f7f7f5;
    --brand-red: #d0021b;
    --brand-red-deep: #b30016;
    --ink: #4a4a4a;
    --ink-soft: #5c5c5c;
    --band: #e3e3e1;
    --band-edge: #ececea;
  }
  * { margin: 0; padding: 0; box-sizing: border-box; }
  html, body {
    width: 1200px;
    height: 900px;
    overflow: hidden;
    background: var(--page);
    font-family: "Open Sans", Arial, sans-serif;
  }
  .sheet {
    position: relative;
    width: 1200px;
    height: 900px;
  }
  .card {
    position: absolute;
    left: 250px;
    width: 700px;
    height: 400px;
    border-radius: 4px;
    box-shadow: 0 2px 8px rgba(0,0,0,0.12);
  }
  .card-back {
    top: 40px;
    background: var(--brand-red);
    display: flex;
    align-items: center;
    justify-content: center;
  }
  .back-wordmark {
    font-size: 84px;
    font-weight: 700;
    letter-spacing: 6px;
    color: var(--brand-red-deep);
    text-transform: uppercase;
  }
  .card-front {
    top: 470px;
    background: var(--card-white);
  }
  .front-wordmark {
    position: absolute;
    top: 92px;
    width: 100%;
    text-align: center;
    font-size: 62px;
    font-weight: 700;
    letter-spacing: 4px;
    color: var(--brand-red);
    text-transform: uppercase;
  }
  .holder-name {
    position: absolute;
    top: 200px;
    width: 100%;
    text-align: center;
    font-size: 24px;
    font-weight: 700;
    color: var(--ink);
  }
  .contact-band {
    position: absolute;
    left: 0;
    right: 0;
    top: 268px;
    height: 84px;
    background: linear-gradient(var(--band-edge), var(--band) 50%, var(--band-edge));
    padding: 12px 34px 0;
    font-size: 16px;
    color: var(--ink-soft);
    line-height: 30px;
  }
  .contact-line { white-space: nowrap; }
  .contact-line:first-child { padding-left: 72px; }
  .label {
    color: var(--brand-red);
    font-weight: 700;
    margin-right: 6px;
  }
  .value { margin-right: 10px; }
</style>
</head>
<body>
  <main class="sheet">
    <section class="card card-back" aria-label="Card back">
      <span class="back-wordmark">Corvimo</span>
    </section>

    <section class="card card-front" aria-label="Card front">
      <div class="front-wordmark">Corvimo</div>
      <div class="holder-name">Daniel Avery</div>
      <div class="contact-band">
        <p class="contact-line">
          <span class="label">Corvimo ltd</span><span class="value">48 Harlow Lane, Brightford ON Canada K2B 4T9</span>
        </p>
        <p class="contact-line">
          <span class="label">Phone</span><span class="value">555 014 2298</span>
          <span class="label">Email</span><span class="value">davery@corvimo.example</span>
          <span class="label">Reg. #</span><span class="value">406183572</span>
        </p>
      </div>
    </section>
  </main>
</body>
</html>
```